Small but growing painting company. Have built up a steady client base. Want to start having a more professional look. Want to start with changing my business cards, and also getting new logo and tee shirts.

Target Market(s)

Home owners, property management companies, all ages 30-70

Industry/Entity Type

Painting And Decorating

Contact Information for Business Card

Bright Ridge Painting LLC Mark Delvecchi 630-584-3907 interior, exterior, vaulted ceiling, drywall repair, pressure washing, kitchen cabinets, epoxy, garage floors,

Font styles to use
Sans Serif
Other font styles liked:
• Harrington

Colors
0355a3
ffffff
ec1f27
000000
3176b5
0493ce
474747
b7b7b7

Requirements
Must have
• Creative, something that doesn’t look like every other painting card.
Nice to have
• I would like something with an arrow or something going to a point

```html
<!DOCTYPE html>
<html lang="en">
<head>
<meta charset="utf-8">
<title>Bright Ridge Painting LLC – Business Cards</title>
<link href="https://fonts.googleapis.com/css2?family=Work+Sans:wght@400;600&display=swap" rel="stylesheet">
<style>
  :root {
    --backdrop: #2b2b2b;
    --card: #1d1d1d;
    --card-edge: #262626;
    --white: #ffffff;
    --brand-blue: #0e6fc4;
    --soft-white: #e9e9e9;
  }
  * { margin: 0; padding: 0; box-sizing: border-box; }
  html, body {
    width: 1200px; height: 900px; overflow: hidden;
    background: var(--backdrop);
    font-family: "Work Sans", Arial, sans-serif;
  }
  .canvas {
    width: 1200px; height: 900px;
    display: flex; flex-direction: column; align-items: center; justify-content: center;
    gap: 44px;
  }
  .card {
    width: 680px; height: 388px;
    background: linear-gradient(135deg, var(--card) 0%, var(--card-edge) 100%);
    border-radius: 3px;
    box-shadow: 0 14px 30px rgba(0,0,0,.45);
    position: relative;
  }
  .card-front { display: flex; align-items: center; justify-content: center; }
  .brand { display: flex; align-items: center; gap: 14px; }
  .brand-mark { width: 22px; height: 22px; background: var(--brand-blue); flex: none; }
  .brand-name {
    color: var(--white); font-weight: 600; font-size: 30px; line-height: 1.15;
  }
  .card-back { display: flex; align-items: center; padding: 0 48px; }
  .card-back .brand { width: 260px; }
  .card-back .brand-name { font-size: 24px; }
  .divider { width: 2px; height: 200px; background: var(--white); margin: 0 36px 0 20px; }
  .contact { color: var(--soft-white); font-size: 17px; letter-spacing: .3px; }
  .contact-name { color: var(--brand-blue); font-size: 30px; letter-spacing: 1.5px; line-height: 1; }
  .contact-role { font-size: 16px; margin: 4px 0 18px; }
  .contact-address { line-height: 1.35; margin-bottom: 14px; }
  .contact-line { display: flex; align-items: center; gap: 10px; line-height: 1.5; }
  .contact-line svg { width: 12px; height: 12px; flex: none; }
  .web-accent { color: var(--brand-blue); }
</style>
</head>
<body>
<main class="canvas">
  <section class="card card-front">
    <div class="brand">
      <span class="brand-mark"></span>
      <span class="brand-name">Bright Ridge<br>Painting LLC</span>
    </div>
  </section>

  <section class="card card-back">
    <div class="brand">
      <span class="brand-mark"></span>
      <span class="brand-name">Bright Ridge<br>Painting LLC</span>
    </div>
    <div class="divider"></div>
    <div class="contact">
      <div class="contact-name">MARK DELVECCHI</div>
      <div class="contact-role">Director</div>
      <div class="contact-address">415 Alder Lane<br>Westfield, IL 60185</div>
      <div class="contact-line">
        <svg viewBox="0 0 12 12"><path d="M2.5 1h2l1 3-1.3 1a6 6 0 0 0 2.8 2.8L8 6.5l3 1v2a1.5 1.5 0 0 1-1.5 1.5A8.5 8.5 0 0 1 1 2.5 1.5 1.5 0 0 1 2.5 1z" fill="#0e6fc4"/></svg>
        <span>630-584-3907</span>
      </div>
      <div class="contact-line">
        <svg viewBox="0 0 12 12"><rect x="1" y="2.5" width="10" height="7" fill="none" stroke="#0e6fc4" stroke-width="1.2"/><path d="M1 2.5l5 4 5-4" fill="none" stroke="#0e6fc4" stroke-width="1.2"/></svg>
        <span>info@brightridgepaint.com</span>
      </div>
      <div class="contact-line">
        <svg viewBox="0 0 12 12"><circle cx="6" cy="6" r="5" fill="none" stroke="#0e6fc4" stroke-width="1.1"/><ellipse cx="6" cy="6" rx="2.2" ry="5" fill="none" stroke="#0e6fc4" stroke-width="1"/><path d="M1 6h10" stroke="#0e6fc4" stroke-width="1"/></svg>
        <span>www.<span class="web-accent">brightridgepaint</span>.com</span>
      </div>
    </div>
  </section>
</main>
</body>
</html>
```